Fresh, modern, fun business card for pediatric dental practice

Need a business card for fresh, modern, fun pediatric dental practice

Clean look that matches our website's font and colors

We prefer the look of curved corners on business cards

Target Market(s)

parents (mothers) of young children, professionals, mid-high class

Industry/Entity Type

Dental

Contact Information for Business Card

Maplebrook Pediatric Dentistry
482 Orchard Vale Road
Suite 517
Harlow Falls, PA 17500
555.419.3067
www.maplebrookkidsdental.example

Mara Tevlin, DMD
Colette Varnum, DMD
(we are working on our email address, but we would like that on the card as well)

Font styles to use
Sans Serif

Requirements
Must have
• All info; we would also like to make cards for individual staff members
• colors from our website and color palatte, attatched
• use same font and design as website for branding
Nice to have
• clean, simple card that has a pop of color
• we would like to see a few designs with our tag line "where smiles get brighter"
• we are not sure if we want to have it on there or not
• we would like to see a few designs incorporating the ribbon graphic on our website where the word WELCOME is

```html
<!DOCTYPE html>
<html lang="en">
<head>
<meta charset="utf-8">
<title>Maplebrook Pediatric Dentistry – Business Card</title>
<link rel="stylesheet" href="https://fonts.googleapis.com/css2?family=Varela+Round&family=Roboto:wght@400&display=swap">
<style>
  :root {
    --backdrop: #2b2b2d;
    --card-white: #ffffff;
    --sun-gold: #f2b623;
    --sun-gold-light: #f7c843;
    --berry: #c8359b;
    --ink-grey: #555559;
    --white: #ffffff;
  }
  * { box-sizing: border-box; margin: 0; padding: 0; }
  html, body { width: 1200px; height: 900px; overflow: hidden; }
  body {
    background: var(--backdrop);
    display: flex;
    align-items: center;
    justify-content: center;
    gap: 60px;
    font-family: "Varela Round", sans-serif;
  }
  .card {
    width: 340px;
    height: 595px;
    border-radius: 22px;
    position: relative;
    overflow: hidden;
    box-shadow: 0 12px 30px rgba(0,0,0,0.45);
  }
  .card--front {
    background: var(--card-white);
    display: flex;
    flex-direction: column;
    align-items: center;
    padding-top: 62px;
  }
  .card--back {
    background: linear-gradient(160deg, var(--sun-gold-light), var(--sun-gold));
    display: flex;
    flex-direction: column;
    align-items: center;
    padding-top: 120px;
  }
  .brand { text-align: center; color: var(--sun-gold); }
  .brand__dot {
    width: 34px; height: 34px; border-radius: 50%;
    background: var(--sun-gold); margin: 0 auto 14px;
  }
  .brand__name {
    font-size: 44px; line-height: 1; letter-spacing: 1px;
  }
  .brand__sub {
    font-size: 20px; letter-spacing: 3px; margin-top: 6px;
    color: var(--berry);
  }
  .card--back .brand,
  .card--back .brand__sub { color: var(--white); }
  .card--back .brand__dot { background: var(--white); }
  .ribbon {
    margin-top: 66px;
    position: relative;
    width: 290px; height: 78px;
  }
  .ribbon svg { position: absolute; inset: 0; }
  .ribbon__name {
    position: absolute; inset: 0;
    display: flex; align-items: center; justify-content: center;
    color: var(--berry); font-size: 27px;
  }
  .contact {
    margin-top: 52px;
    text-align: center;
    font-family: "Roboto", sans-serif;
    color: var(--ink-grey);
    font-size: 15px;
    line-height: 1.45;
  }
  .contact__icons { display: flex; gap: 6px; justify-content: center; margin-bottom: 10px; }
  .contact__rule {
    width: 150px; height: 2px; background: var(--sun-gold);
    margin: 16px auto;
  }
</style>
</head>
<body>
  <section class="card card--front">
    <div class="brand">
      <div class="brand__dot"></div>
      <div class="brand__name">maplebrook</div>
      <div class="brand__sub">pediatric dentistry</div>
    </div>

    <div class="ribbon">
      <svg viewBox="0 0 290 78" width="290" height="78" aria-hidden="true">
        <path d="M8 0 H282 V14 Q290 39 282 64 V78 H8 V64 Q0 39 8 14 Z" fill="#f2b623"/>
        <rect x="18" y="10" width="254" height="58" rx="20" fill="none" stroke="#ffffff" stroke-width="2" stroke-dasharray="3 5"/>
      </svg>
      <div class="ribbon__name">Mara Tevlin, DMD</div>
    </div>

    <div class="contact">
      <div class="contact__icons">
        <svg width="24" height="24" viewBox="0 0 24 24" aria-label="Phone" role="img">
          <circle cx="12" cy="12" r="12" fill="#c8359b"/>
          <path d="M8.5 6.5 l2 2 -1.2 1.4 q1 2.3 3.6 3.6 l1.4-1.2 2 2 -1.5 1.7 q-4.5-0.5-8-6 z" fill="#fff"/>
        </svg>
        <svg width="24" height="24" viewBox="0 0 24 24" aria-label="Email" role="img">
          <circle cx="12" cy="12" r="12" fill="#c8359b"/>
          <rect x="6" y="8" width="12" height="8" fill="#fff"/>
          <path d="M6 8 L12 13 L18 8" fill="none" stroke="#c8359b" stroke-width="1.2"/>
        </svg>
        <svg width="24" height="24" viewBox="0 0 24 24" aria-label="Website" role="img">
          <circle cx="12" cy="12" r="12" fill="#c8359b"/>
          <circle cx="12" cy="12" r="6" fill="none" stroke="#fff" stroke-width="1.3"/>
          <ellipse cx="12" cy="12" rx="2.6" ry="6" fill="none" stroke="#fff" stroke-width="1.1"/>
          <line x1="6" y1="12" x2="18" y2="12" stroke="#fff" stroke-width="1.1"/>
        </svg>
      </div>
      <p>555.419.3067</p>
      <p>info@maplebrookkidsdental.example</p>
      <p>www.maplebrookkidsdental.example</p>
      <div class="contact__rule"></div>
      <p>482 Orchard Vale Road, Suite 517</p>
      <p>Harlow Falls, PA 17500</p>
    </div>
  </section>

  <section class="card card--back">
    <div class="brand">
      <div class="brand__dot"></div>
      <div class="brand__name">maplebrook</div>
      <div class="brand__sub">pediatric dentistry</div>
    </div>
  </section>
</body>
</html>
```